EARLY OUT TO BAD DEBT FLOW CHART

Marketing Tool for Conferences

Target Market(s)

Healthcare providers

Requirements
Must have
• Logo
Nice to have
• Complete redesign, updated

```html
<!DOCTYPE html>
<html lang="en">
<head>
<meta charset="utf-8">
<title>Early Out to Bad Debt Flow Chart</title>
<link href="https://fonts.googleapis.com/css2?family=Oswald:wght@300;400;600&family=Pathway+Gothic+One&display=swap" rel="stylesheet">
<style>
  :root {
    --bg-top: #e3f1fa;
    --bg-bottom: #f5f9fc;
    --title-red: #e4202a;
    --track: #b4b8bc;
    --teal: #23b8c5;
    --teal-light: #7dcfe6;
    --lime: #9ccc3c;
    --yellow: #e0df1c;
    --orchid: #d466a6;
    --orchid-light: #ea8fbf;
    --green: #00a651;
    --green-light: #8cc965;
    --sky: #12b5e3;
    --pink: #e8378e;
    --pink-light: #f5b3d0;
    --red: #e8363f;
    --red-light: #f26268;
    --purple: #5b3e8f;
    --purple-light: #8866b0;
    --logo-grey: #56635f;
  }
  * { margin: 0; padding: 0; box-sizing: border-box; }
  html, body { width: 1200px; height: 855px; overflow: hidden; }
  body {
    position: relative;
    background: linear-gradient(160deg, var(--bg-top) 0%, var(--bg-bottom) 55%, #e6f3fa 100%);
    font-family: "Oswald", sans-serif;
  }
  .diagram { position: absolute; inset: 0; width: 1200px; height: 855px; }
  .label {
    position: absolute;
    display: flex;
    align-items: center;
    justify-content: center;
    text-align: center;
    color: #fff;
    font-family: "Pathway Gothic One", "Oswald", sans-serif;
    font-weight: 400;
    font-size: 11px;
    line-height: 1.1;
    white-space: nowrap;
    border-radius: 6px;
    padding: 2px 3px;
  }
  .label--teal { background: var(--teal); }
  .label--lime { background: var(--lime); }
  .label--orchid { background: var(--orchid); }
  .label--green { background: var(--green); }
  .label--pink { background: var(--pink); }
  .label--red { background: var(--red); }
  .label--purple { background: var(--purple); }
  .label--big { font-size: 12.5px; }
  .process-title {
    position: absolute;
    text-align: center;
    color: var(--title-red);
    line-height: 1;
    width: 200px;
  }
  .process-title__strong { display: block; font-weight: 600; font-size: 33px; }
  .process-title__light { display: block; font-weight: 300; font-size: 32px; margin-top: 3px; }
  .brand {
    position: absolute;
    left: 880px;
    top: 712px;
    display: flex;
    align-items: center;
    gap: 16px;
  }
  .brand__dot { width: 56px; height: 56px; border-radius: 50%; background: var(--logo-grey); }
  .brand__name {
    color: var(--logo-grey);
    font-weight: 400;
    font-size: 25px;
    line-height: 1.08;
    letter-spacing: 1px;
  }
</style>
</head>
<body>
<svg class="diagram" viewBox="0 0 1200 855" xmlns="http://www.w3.org/2000/svg">
  <defs>
    <filter id="node-shadow" x="-30%" y="-30%" width="160%" height="160%">
      <feDropShadow dx="3" dy="4" stdDeviation="3" flood-color="#000" flood-opacity="0.25"/>
    </filter>
  </defs>

  <g class="track" fill="none" stroke="var(--track)" stroke-width="3" stroke-dasharray="9 7">
    <path d="M600 273 A151 151 0 1 1 752 424"/>
    <path d="M448 430 A152 152 0 1 0 600 582"/>
    <line x1="600" y1="273" x2="600" y2="582"/>
  </g>

  <g class="connectors" fill="none" stroke-width="2" stroke-dasharray="0.1 4" stroke-linecap="round">
    <polyline stroke="var(--teal)" points="621,90 645,90 645,132"/>
    <polyline stroke="var(--lime)" points="752,88 752,78 783,78"/>
    <polyline stroke="var(--orchid)" points="927,136 927,164 892,164"/>
    <polyline stroke="var(--green)" points="937,273 942,273 942,354"/>
    <polyline stroke="var(--pink)" points="859,416 859,452"/>
    <polyline stroke="var(--red)" points="734,361 752,361 752,390"/>
    <polyline stroke="var(--purple)" points="534,238 534,280 567,280"/>
    <polyline stroke="var(--green)" points="554,432 554,390 567,390"/>
    <polyline stroke="var(--orchid)" points="645,530 645,582 634,582"/>
    <polyline stroke="var(--red)" points="448,465 448,495 480,495"/>
    <polyline stroke="var(--pink)" points="341,405 341,441"/>
    <polyline stroke="var(--green)" points="257,502 257,582 263,582"/>
    <polyline stroke="var(--lime)" points="272,725 272,690 307,690"/>
    <polyline stroke="var(--teal)" points="418,777 447,777 447,768"/>
    <polyline stroke="var(--purple)" points="555,725 555,764 574,764"/>
  </g>

  <g class="node node--scrubbed" transform="translate(645 166)" filter="url(#node-shadow)">
    <circle r="33" fill="var(--teal)"/><circle r="28" fill="var(--teal-light)"/>
    <rect x="-16" y="-14" width="32" height="22" rx="2" fill="none" stroke="#fff" stroke-width="2.5"/>
    <text x="0" y="3" fill="#fff" font-family="Oswald, sans-serif" font-weight="600" font-size="15" text-anchor="middle">01</text>
    <rect x="-2" y="8" width="4" height="6" fill="#fff"/><rect x="-8" y="13" width="16" height="3" fill="#fff"/>
  </g>
  <g class="node node--validation" transform="translate(752 122)" filter="url(#node-shadow)">
    <circle r="33" fill="var(--lime)"/><circle r="28" fill="var(--yellow)"/>
    <rect x="-17" y="-12" width="34" height="28" rx="3" fill="none" stroke="#fff" stroke-width="2.5"/>
    <rect x="-10" y="-18" width="4" height="9" rx="2" fill="#fff"/><rect x="-2" y="-18" width="4" height="9" rx="2" fill="#fff"/><rect x="6" y="-18" width="4" height="9" rx="2" fill="#fff"/>
    <text x="0" y="12" fill="#fff" font-family="Oswald, sans-serif" font-weight="600" font-size="17" text-anchor="middle">30</text>
  </g>
  <g class="node node--letters-more" transform="translate(859 166)" filter="url(#node-shadow)">
    <circle r="33" fill="var(--orchid)"/><circle r="28" fill="var(--orchid-light)"/>
    <polygon points="-16,2 16,-16 6,16 0,6" fill="#fff"/>
    <polyline points="16,-16 0,6 -2,14" fill="none" stroke="var(--orchid-light)" stroke-width="2"/>
  </g>
  <g class="node node--calls" transform="translate(903 273)" filter="url(#node-shadow)">
    <circle r="33" fill="var(--green)"/><circle r="28" fill="var(--sky)"/>
    <path d="M-16 -6 q16 -12 32 0 l-3 6 -7 -2 0 -4 q-6 -2 -12 0 l0 4 -7 2z" fill="#fff"/>
    <rect x="-13" y="2" width="26" height="14" rx="3" fill="#fff"/>
    <g fill="var(--sky)"><rect x="-6" y="6" width="3" height="2"/><rect x="-1.5" y="6" width="3" height="2"/><rect x="3" y="6" width="3" height="2"/><rect x="-6" y="10" width="3" height="2"/><rect x="-1.5" y="10" width="3" height="2"/><rect x="3" y="10" width="3" height="2"/></g>
  </g>
  <g class="node node--emails" transform="translate(859 380)" filter="url(#node-shadow)">
    <circle r="33" fill="var(--pink)"/><circle r="28" fill="var(--pink-light)"/>
    <rect x="-8" y="-12" width="26" height="20" rx="2" fill="#fff"/>
    <polyline points="-8,-12 5,-1 18,-12" fill="none" stroke="var(--pink-light)" stroke-width="2"/>
    <rect x="-20" y="-4" width="9" height="3" rx="1.5" fill="#fff"/><rect x="-18" y="2" width="7" height="3" rx="1.5" fill="#fff"/>
  </g>
  <g class="node node--hibernate" transform="translate(752 424)" filter="url(#node-shadow)">
    <circle r="33" fill="var(--red)"/><circle r="28" fill="var(--red-light)"/>
    <circle r="19" fill="none" stroke="#fff" stroke-width="5"/>
    <rect x="-3" y="-12" width="6" height="20" rx="3" fill="#fff"/>
  </g>
  <g class="node node--begin" transform="translate(600 273)" filter="url(#node-shadow)">
    <circle r="33" fill="var(--purple)"/><circle r="28" fill="var(--purple-light)"/>
    <circle cx="1" cy="-12" r="8" fill="none" stroke="#fff" stroke-width="2"/>
    <text x="1" y="-8" fill="#fff" font-family="Oswald, sans-serif" font-size="11" text-anchor="middle">$</text>
    <path d="M-16 14 l8 -10 q6 -3 12 1 l6 0 q3 2 0 4 l-8 0 l10 0 l10 -7 q3 0 2 3 l-12 11 l-16 0 l-5 5z" fill="#fff"/>
  </g>
  <g class="node node--moved" transform="translate(600 390)" filter="url(#node-shadow)">
    <circle r="33" fill="var(--green)"/><circle r="28" fill="var(--green-light)"/>
    <path d="M-17 -13 h10 l4 4 h20 v22 h-34z" fill="none" stroke="#fff" stroke-width="2.5" stroke-linejoin="round"/>
    <line x1="-8" y1="2" x2="8" y2="2" stroke="#fff" stroke-width="2.5" stroke-linecap="round"/>
    <polyline points="3,-4 9,2 3,8" fill="none" stroke="#fff" stroke-width="2.5" stroke-linecap="round" stroke-linejoin="round"/>
  </g>

  <g class="node node--received" transform="translate(448 430)" filter="url(#node-shadow)">
    <circle r="33" fill="var(--red)"/><circle r="28" fill="var(--red-light)"/>
    <circle r="20" fill="#fff"/>
    <circle cx="0" cy="-7" r="6" fill="var(--red)"/>
    <path d="M-11 10 q0 -10 11 -10 q11 0 11 10z" fill="var(--red)"/>
  </g>
  <g class="node node--payments" transform="translate(341 475)" filter="url(#node-shadow)">
    <circle r="33" fill="var(--pink)"/><circle r="28" fill="var(--pink-light)"/>
    <g transform="rotate(-18)">
      <rect x="-17" y="-4" width="26" height="14" rx="1" fill="none" stroke="#fff" stroke-width="2"/>
      <rect x="-13" y="2" width="26" height="14" rx="1" fill="#fff"/>
      <circle cx="0" cy="9" r="3.5" fill="var(--pink-light)"/>
    </g>
    <path d="M2 -8 l10 -8 l5 5 l-9 9 z" fill="#fff"/>
  </g>
  <g class="node node--clean-bill" transform="translate(297 582)" filter="url(#node-shadow)">
    <circle r="33" fill="var(--green)"/><circle r="28" fill="var(--green-light)"/>
    <rect x="-16" y="-15" width="22" height="30" rx="2" fill="none" stroke="#fff" stroke-width="2.2"/>
    <g stroke="#fff" stroke-width="2"><line x1="-11" y1="-8" x2="1" y2="-8"/><line x1="-11" y1="-3" x2="1" y2="-3"/><line x1="-11" y1="2" x2="-2" y2="2"/><line x1="-11" y1="7" x2="-2" y2="7"/></g>
    <circle cx="9" cy="3" r="8" fill="var(--green-light)" stroke="#fff" stroke-width="2"/>
    <text x="9" y="7.5" fill="#fff" font-family="Oswald, sans-serif" font-weight="600" font-size="12" text-anchor="middle">$</text>
  </g>
  <g class="node node--three-letters" transform="translate(341 689)" filter="url(#node-shadow)">
    <circle r="33" fill="var(--lime)"/><circle r="28" fill="var(--yellow)"/>
    <rect x="-15" y="-15" width="24" height="30" rx="2" fill="none" stroke="#fff" stroke-width="2.2"/>
    <g stroke="#fff" stroke-width="2"><line x1="-10" y1="-9" x2="4" y2="-9"/><line x1="-10" y1="-4" x2="4" y2="-4"/><line x1="-10" y1="1" x2="2" y2="1"/><line x1="-10" y1="6" x2="0" y2="6"/></g>
    <line x1="16" y1="-13" x2="2" y2="9" stroke="#fff" stroke-width="4" stroke-linecap="round"/>
  </g>
  <g class="node node--phone-weekly" transform="translate(448 733)" filter="url(#node-shadow)">
    <circle r="33" fill="var(--teal)"/><circle r="28" fill="var(--teal-light)"/>
    <circle r="20" fill="none" stroke="#fff" stroke-width="2.5"/>
    <path d="M-9 -11 l5 -1 l3 7 l-3 3 q2 6 8 8 l3 -3 l7 3 l-1 5 q-2 2 -5 2 q-16 -3 -19 -19 q0 -3 2 -5z" fill="#fff"/>
  </g>
  <g class="node node--email-weekly" transform="translate(555 689)" filter="url(#node-shadow)">
    <circle r="33" fill="var(--purple)"/><circle r="28" fill="var(--purple-light)"/>
    <circle r="23" fill="#fff"/>
    <rect x="-13" y="-9" width="26" height="18" rx="1.5" fill="var(--purple-light)"/>
    <polyline points="-13,-9 0,2 13,-9" fill="none" stroke="#fff" stroke-width="2"/>
  </g>
  <g class="node node--unresolved" transform="translate(600 582)" filter="url(#node-shadow)">
    <circle r="33" fill="var(--orchid)"/><circle r="28" fill="var(--orchid-light)"/>
    <path d="M-15 -16 h30 v26 h-11 l-4 5 l-4 -5 h-11z" fill="#fff"/>
    <circle cx="0" cy="-7" r="5" fill="var(--orchid-light)"/>
    <path d="M-9 6 q0 -8 9 -8 q9 0 9 8z" fill="var(--orchid-light)"/>
  </g>
</svg>

<div class="process-title" style="left:656px; top:231px;">
  <span class="process-title__strong">COLLECTION</span>
  <span class="process-title__light">PROCESS</span>
</div>
<div class="process-title" style="left:348px; top:553px;">
  <span class="process-title__strong">EARLY OUT</span>
  <span class="process-title__light">PROCESS</span>
</div>

<div class="label label--teal" style="left:541px; top:75px; width:78px; height:31px;">Account is scrubbed<br>and scored</div>
<div class="label label--lime" style="left:784px; top:61px; width:86px; height:33px;">30 day validation<br>letter is sent</div>
<div class="label label--orchid" style="left:893px; top:91px; width:70px; height:44px;">A series of more<br>collection letters<br>re sent</div>
<div class="label label--green" style="left:908px; top:355px; width:70px; height:48px;">Collection phone<br>calls<br>are made weekly</div>
<div class="label label--pink" style="left:834px; top:453px; width:50px; height:27px;">Emails are<br>sent weekly</div>
<div class="label label--red" style="left:666px; top:351px; width:67px; height:20px;">Hibernate account</div>
<div class="label label--purple" style="left:499px; top:205px; width:70px; height:31px;">Collections Begin</div>
<div class="label label--green" style="left:519px; top:434px; width:70px; height:31px;">Account is moved<br>to collections</div>
<div class="label label--orchid" style="left:611px; top:472px; width:70px; height:56px;">If account is not<br>resolved<br>within 60 days<br>of placement</div>
<div class="label label--red label--big" style="left:481px; top:483px; width:85px; height:23px;">Account is Received</div>
<div class="label label--pink label--big" style="left:299px; top:372px; width:85px; height:33px;">Payments and<br>adjustment applied</div>
<div class="label label--green label--big" style="left:223px; top:453px; width:70px; height:47px; text-align:left;">1st clean bill is<br>sent to patient</div>
<div class="label label--lime" style="left:239px; top:727px; width:67px; height:30px;">A series of<br>3 letters are sent</div>
<div class="label label--teal" style="left:347px; top:761px; width:69px; height:33px;">Phone calls are<br>made weekly</div>
<div class="label label--purple" style="left:576px; top:748px; width:46px; height:33px;">emails are<br>sent weekly</div>

<div class="brand">
  <span class="brand__dot"></span>
  <span class="brand__name">Harborline<br>Recovery<br>Group</span>
</div>
</body>
</html>
```